Brisvane Partners Web Design

Dear all
I need a web design for a financial services site. We are a broker who deals with many different financial institutions and require a clean, simple and instantly impressive site based on the colour scheme that Mockwell created for us. A landing page (www.brisvn.mx) gives an idea of the logo and clour scheme but we are looking at either a one page site with rollover text boxes or a 3 or 4 page site depending on the preference of the designer and the best user experience. The site“s purpose is to give confidence that the company exists rather than impart pages of information although we would like this to be a site that can expand over time as the company grows. For now the requirement is for a clear set of possibly changing images at the centre of a white screen that relate to finance in general nad the benefits of wealth creation as well as sectios either along the top or bottom - Our Company, Our Approach, Our services, Our clients, Contact (user to fill in contact box to be sent to info@brisvn.mx. The text for each of these boxes I assume can be added by the coding team here, it the overall look and feel that I am looking for from Mockwell - deadline can be extended if necessary but I was hoping to wrap this all up in October

Target Market(s)

Succesful individuals looking to maximise returns on their investment via world class financial institutions and supported throughout by qualified independent financial advisors

Industry/Entity Type

Finance

Requirements
Must have
• Logo and color scheme of the logo design Mockwell sent - I have all these sourcefiles, pantone and fonts

```html
<!DOCTYPE html>
<html lang="en">
<head>
<meta charset="utf-8">
<title>Brisvane Partners</title>
<link rel="stylesheet" href="https://fonts.googleapis.com/css2?family=Comfortaa:wght@300;400&family=Roboto:wght@400;500;700&display=swap">
<style>
:root{
  --navy:#1f3a60;
  --orange:#f0a032;
  --page:#efefef;
  --card-head:#f3f3f3;
  --text:#4a4a4a;
  --footer-nav:#6f777b;
  --footer:#868d91;
  --white:#ffffff;
}
*{margin:0;padding:0;box-sizing:border-box}
html,body{width:1200px;height:1092px;overflow:hidden}
body{position:relative;background:var(--white);font-family:"Roboto",Arial,sans-serif;color:var(--text)}
.abs{position:absolute}
.header{left:0;top:0;width:1200px;height:141px;background:linear-gradient(#ffffff,#f1f2f4)}
.navbar{left:0;top:141px;width:1200px;height:26px;background:var(--navy)}
.brand{left:170px;top:0;width:260px;height:167px;background:var(--white);box-shadow:0 0 4px rgba(0,0,0,.12);display:flex;align-items:center;justify-content:center;gap:10px;z-index:3}
.brand-dot{width:22px;height:22px;border-radius:50%;background:var(--navy)}
.brand-name{font-family:"Comfortaa",sans-serif;font-weight:400;font-size:19px;color:var(--navy)}
.call{left:845px;top:46px;width:186px;height:40px}
.call-text{position:absolute;right:0;top:4px;text-align:right}
.call-label{font-size:10.5px;color:#555}
.call-number{font-size:16px;font-weight:700;color:var(--navy);margin-top:2px}
.menu{left:448px;top:141px;height:26px;display:flex;list-style:none}
.menu li{font-size:11px;color:var(--white);line-height:26px;padding:0 13px;border-right:1px solid #3d5578}
.menu li:last-child{border-right:none}
.menu li.active{background:var(--orange);padding:0 14px}
.hero{left:0;top:167px;width:1200px;height:360px;background:linear-gradient(120deg,#2c4466 0%,#8ea3bf 30%,#c7d3e2 55%,#b5c4d7 80%,#8799b2 100%)}
.tag{right:169px;background:var(--orange);color:var(--white);font-family:"Comfortaa",sans-serif;font-weight:300;font-size:23px;letter-spacing:1px;height:36px;line-height:36px;padding:0 13px}
.tag-1{top:263px}
.tag-2{top:307px}
.content{left:0;top:527px;width:1200px;height:380px;background:var(--page)}
.card{top:418px;width:204px;height:279px;background:var(--white);box-shadow:0 6px 6px -3px rgba(0,0,0,.25)}
.card-title{height:34px;background:var(--card-head);font-family:"Comfortaa",sans-serif;font-size:16.5px;letter-spacing:.5px;color:var(--navy);text-align:center;line-height:38px}
.card-photo{position:absolute;left:14px;top:49px;width:176px;height:110px}
.card-text{position:absolute;left:12px;top:172px;width:180px;font-size:11.3px;line-height:14px;text-align:center;color:var(--text)}
.card-btn{position:absolute;left:14px;top:239px;width:176px;height:25px;background:var(--navy);color:var(--white);font-size:11.5px;text-align:center;line-height:25px}
.welcome{left:0;top:735px;width:1200px;text-align:center;font-family:"Comfortaa",sans-serif;font-size:24px;letter-spacing:1.5px;color:var(--navy)}
.rule{left:220px;top:777px;width:760px;height:1px;background:linear-gradient(90deg,transparent,#d3d3d3,transparent)}
.intro{left:200px;width:800px;text-align:center;font-size:11.3px;line-height:14px;color:var(--text)}
.intro-1{top:795px}
.intro-2{top:878px}
.footer-nav{left:0;top:956px;width:1200px;height:44px;background:var(--footer-nav);display:flex;justify-content:center;align-items:center;font-size:11.5px;color:var(--white)}
.footer-nav span.sep{margin:0 17px;color:#b8bec1}
.footer{left:0;top:1000px;width:1200px;height:92px;background:var(--footer);color:var(--white);text-align:center}
.footer h2{margin-top:19px;font-size:17.5px;font-weight:500}
.footer .line{width:320px;height:1px;margin:6px auto 0;background:linear-gradient(90deg,transparent,#b4b9bc,transparent)}
.footer p{margin-top:11px;font-size:11.5px}
.footer p b{font-weight:700}
.footer p .sep{margin:0 15px;color:#bcc1c4}
</style>
</head>
<body>
<div class="abs header"></div>
<div class="abs navbar"></div>

<div class="abs brand"><span class="brand-dot"></span><span class="brand-name">Brisvane Partners</span></div>

<div class="abs call">
  <svg width="37" height="37" viewBox="0 0 37 37" aria-hidden="true">
    <circle cx="18.5" cy="18.5" r="17" fill="none" stroke="#c9c9c9" stroke-width="1.6"/>
    <path d="M13 10c1.5-1 3-.8 3.6.6l1.3 3c.4 1-.1 1.8-1 2.3l-1 .6c.7 2.3 2 4.3 3.9 5.8l.9-.7c.8-.6 1.8-.6 2.4.3l1.9 2.6c.8 1.2.3 2.5-1 3.2-3.6 1.9-8.5-1.5-11-6.7-1.9-4-1.6-9.5 0-11z" fill="none" stroke="#bdbdbd" stroke-width="1.4"/>
  </svg>
  <div class="call-text">
    <div class="call-label">Feel free to call us</div>
    <div class="call-number">+52 (55) 4190 2275</div>
  </div>
</div>

<ul class="abs menu">
  <li class="active">HOME</li>
  <li>OUR COMPANY</li>
  <li>OUR APPROACH</li>
  <li>OUR SERVICES</li>
  <li>OUR CLIENTS</li>
  <li>CONTACT US</li>
</ul>

<div class="abs hero" role="img" aria-label="Finance photo: calculator keys, stock chart printout and stacked coins in blue tones"></div>
<div class="abs tag tag-1">Offering The Most</div>
<div class="abs tag tag-2">Compatitive Rates &amp; Fees</div>

<div class="abs content"></div>

<div class="abs card" style="left:170px">
  <div class="card-title">OUR COMPANY</div>
  <div class="card-photo" role="img" aria-label="Glass office tower seen from below" style="background:linear-gradient(135deg,#a9c6e2,#2f5f8f 60%,#17324f)"></div>
  <div class="card-text">Lorem ipsum dolor sit amet, con-sectetur adipisicing elit, sed do eiusmod tempor incididunt ut labore et dolore....</div>
  <div class="card-btn">Read More</div>
</div>
<div class="abs card" style="left:389px">
  <div class="card-title">OUR APPROACH</div>
  <div class="card-photo" role="img" aria-label="Advisor with headset working at a computer" style="background:linear-gradient(135deg,#e8e8e8,#c9cdd3 60%,#8a8f96)"></div>
  <div class="card-text">Lorem ipsum dolor sit amet, con-sectetur adipisicing elit, sed do eiusmod tempor incididunt ut labore et dolore....</div>
  <div class="card-btn">Read More</div>
</div>
<div class="abs card" style="left:608px">
  <div class="card-title">OUR SERVICES</div>
  <div class="card-photo" role="img" aria-label="Business people assembling large puzzle pieces" style="background:linear-gradient(135deg,#f0f0f0,#d6d8db 55%,#7b7f85)"></div>
  <div class="card-text">Lorem ipsum dolor sit amet, con-sectetur adipisicing elit, sed do eiusmod tempor incididunt ut labore et dolore....</div>
  <div class="card-btn">Read More</div>
</div>
<div class="abs card" style="left:828px">
  <div class="card-title">OUR CLIENTS</div>
  <div class="card-photo" role="img" aria-label="Group of smiling business clients" style="background:linear-gradient(135deg,#e4ecf3,#b8a596 50%,#2a2d33)"></div>
  <div class="card-text">Lorem ipsum dolor sit amet, con-sectetur adipisicing elit, sed do eiusmod tempor incididunt ut labore et dolore....</div>
  <div class="card-btn">Read More</div>
</div>

<h1 class="abs welcome" style="font-weight:300">Welcome to Our Site</h1>
<div class="abs rule"></div>
<p class="abs intro intro-1">Lorem ipsum dolor sit amet, consectetur adipisicing elit, sed do eiusmod tempor incididunt ut labore et dolore magna aliqua. Ut enim ad minim veniam,<br>quis nostrud exercitation ullamco laboris nisi ut aliquip ex ea commodo consequat. Duis aute irure dolor in reprehenderit in<br>voluptate velit esse cillum dolore eu fugiat nulla pariatur. Excepteur sint occaecat cupidatat non proident,<br>sunt in culpa qui officia deserunt mollit anim id est laborum.</p>
<p class="abs intro intro-2">Lorem ipsum dolor sit amet, consectetur adipisicing elit, sed do eiusmod tempor incididunt ut labore et dolore magna aliqua.<br>Ut enim ad minim veniam, quis nostrud exercitation ullamco laboris nisi ut aliquip ex ea commodo consequat.</p>

<nav class="abs footer-nav">
  <span>Home</span><span class="sep">|</span><span>Our Company</span><span class="sep">|</span><span>Our Approach</span><span class="sep">|</span><span>Our services</span><span class="sep">|</span><span>Our clients</span><span class="sep">|</span><span>Contact us</span>
</nav>

<footer class="abs footer">
  <h2>Get In Touch</h2>
  <div class="line"></div>
  <p><b>Tel :</b> +52 (55) 4190 2275<span class="sep">|</span><b>Email :</b> info@brisvn.mx</p>
</footer>
</body>
</html>
```